Independent Midwife for a positive birth experience needs a vibrant, and elegant business card/logo

I need a business card design with a logo. The logo I would like to be able to use on my website (www.midwifeorlaith.com) next to my name.
Therefore the design of the card and logo should suit the colours and design of the website. The title of the website and company is "Orlaith Denby Marsworth, Midwife" but I'd like to have the business card title to be "Orlaith Denby Marsworth - Independent Midwife" in bold letters, same script font as in my website.

I provide gold standard midwifery services, one-to-one tailored care, continuity of care throughout the entire pregnancy (antenatal care), the birth and after the birth (postnatal care), home birth, water birth, breast-feeding support, and birth preparation workshops. I also am certified and offer complementary therapies: pregnancy reflexology, rebozo techniques for optimal baby positioning.

The design should incorporate similar colours and style as the website and the "Orlaith Denby Marsworth - Independent Midwife" on the card should include the same font as in the title of the website, however, in bold. The front of the card should have a logo, title and contact information (phone number 071592604, email orlaith.marsworth@quillpost.com, website address www.midwifeorlaith.com).
The back of the card to include the services I offer.

The logo: use of colour purple (varying shades), should communicate communicate warmth, kindness, compassion. It should convey that I'm a midwife who believes in fostering a trusting relationship with my clients and to provide them with a positive pregnancy and birth experience.

Target Market(s)

Pregnant women or women who are looking to book a private midwife for better birth experience and outcome

Industry/Entity Type

Baby

Contact Information for Business Card

Name and Title on front side together with contact details
The reverse side should have services/packages offered

Font styles to use
Script
Other font styles liked:
• similar script as in my website for name and title, and easy to read font for the rest of the words

Colors
b768aa
a54599
d2a4cc
ffffff

Requirements
Must have
• same font as title of website, but slightly bolder.
• similar design, colours, patterns as in website.
• Also include a gold accent colour somewhere in the design please.
Nice to have
• perhaps a logo of pregnant belly in profile or newborn baby icon

```html
<!DOCTYPE html>
<html lang="en">
<head>
<meta charset="utf-8">
<title>Orlaith Denby Marsworth - Independent Midwife - Business Card</title>
<link rel="stylesheet" href="https://fonts.googleapis.com/css2?family=Niconne&family=Lato:wght@300;400&display=swap">
<style>
  :root {
    --plum: #a34596;
    --lilac: #e6cfe3;
    --script-tint: #dcb5d6;
    --label-tint: #dcbfd8;
    --text-light: #f1e2ef;
    --rule: #c98bbf;
    --page: #ffffff;
    --edge: #9a9a9a;
  }
  * { margin: 0; padding: 0; box-sizing: border-box; }
  html, body {
    width: 1200px; height: 900px; overflow: hidden;
    background: var(--page);
  }
  .canvas { position: relative; width: 1200px; height: 900px; }
  .card {
    position: absolute; left: 246px; width: 690px; height: 399px;
    background: var(--plum);
    outline: 1px solid var(--edge);
    overflow: hidden;
  }
  .card--front { top: 37px; }
  .card--back { top: 457px; }
  .card__corner { position: absolute; inset: 0; }
  .logo-mark {
    position: absolute; left: 22px; top: 26px; width: 170px; height: 305px;
    border-radius: 40% 60% 55% 45% / 30% 50% 50% 70%;
    background: radial-gradient(ellipse at 60% 55%, rgba(230,207,227,0.35), rgba(230,207,227,0.08) 70%, transparent);
  }
  .title {
    position: absolute; left: 200px; width: 460px; text-align: center;
    font-family: "Niconne", cursive; color: var(--script-tint);
  }
  .title__name { top: 118px; font-size: 40px; line-height: 1; }
  .title__role { top: 190px; left: 218px; font-size: 34px; line-height: 1; }
  .contact {
    position: absolute; left: 190px; top: 262px;
    display: grid; grid-template-columns: 68px 1px auto; column-gap: 14px;
    font-family: "Lato", sans-serif; font-size: 15px; line-height: 22.5px;
  }
  .contact__labels { text-align: right; color: var(--label-tint); }
  .contact__rule { background: var(--rule); height: 80px; }
  .contact__values { color: var(--label-tint); font-weight: 300; }
  .accent-sweep {
    position: absolute; left: 110px; top: 0; width: 150px; height: 399px;
    background: linear-gradient(100deg, transparent 20%, rgba(230,207,227,0.18) 50%, transparent 80%);
  }
  .services {
    position: absolute; left: 246px; top: 63px; list-style: none;
    font-family: "Lato", sans-serif; font-weight: 300; font-size: 24px;
    line-height: 33.7px; color: var(--text-light);
  }
</style>
</head>
<body>
<main class="canvas">
  <section class="card card--front">
    <svg class="card__corner" viewBox="0 0 690 399" aria-hidden="true">
      <path d="M690,190 C690,320 610,399 500,399 L690,399 Z" fill="var(--lilac)"/>
    </svg>
    <div class="logo-mark" role="img" aria-label="Logo area: pregnant figure in profile, drawn in soft lilac lines"></div>
    <h1 class="title title__name">Orlaith Denby Marsworth</h1>
    <h2 class="title title__role">Independent Midwife</h2>
    <div class="contact">
      <div class="contact__labels">phone<br>email<br>website</div>
      <div class="contact__rule"></div>
      <div class="contact__values">071592604<br>orlaith.marsworth@quillpost.com<br>www.midwifeorlaith.com</div>
    </div>
  </section>

  <section class="card card--back">
    <svg class="card__corner" viewBox="0 0 690 399" aria-hidden="true">
      <path d="M0,205 C20,330 90,399 180,399 L0,399 Z" fill="var(--lilac)"/>
    </svg>
    <div class="accent-sweep" role="img" aria-label="Faint decorative sweep echoing the logo figure"></div>
    <ul class="services">
      <li>Gold Standard Midwifery Services</li>
      <li>One-to-one tailored care</li>
      <li>Antenatal care</li>
      <li>Postnatal care</li>
      <li>Home Birth &amp; Water Birth</li>
      <li>Breast-feeding support</li>
      <li>Birth preparation workshops</li>
      <li>Certified in complementary therapies</li>
    </ul>
  </section>
</main>
</body>
</html>
```